Veradock Stationary
Cards, letterhead, envelopes
Simple
Calvin Dufresne
General Manager
4271 Harrowmill Road, Suite 100
Oceanside CA, 92743
Use place holder
Use Place Holder
cdufresne@veradockpanes.example
www.veradockpanes.example
Play with a 1 sided vs 2 sided options for business cards. I am open to both. Need stationary as well.
Use this logo
.ai version

```html
<!DOCTYPE html>
<html lang="en">
<head>
<meta charset="utf-8">
<title>Veradock Stationary</title>
<link rel="stylesheet" href="https://fonts.googleapis.com/css2?family=Open+Sans:wght@400;600;700&display=swap">
<style>
:root{
  --bg:#ecebe8;
  --paper:#ffffff;
  --brown:#7a4a22;
  --copper:#c0732a;
  --ink:#4a4a4a;
  --muted:#8a8a8a;
  --rule:#cfcfcf;
  --slate:#6b6d70;
  --slate-dark:#4c4e51;
}
*{box-sizing:border-box;margin:0;padding:0}
html,body{width:1200px;height:899px;overflow:hidden;background:var(--bg);font-family:"Open Sans",Arial,sans-serif;color:var(--ink)}
.canvas{position:relative;width:1200px;height:899px}
.sheet{position:absolute;background:var(--paper);box-shadow:0 2px 8px rgba(0,0,0,.18)}

/* brand lockup */
.brand{display:flex;align-items:center;gap:7px}
.brand-dot{width:22px;height:22px;border-radius:50%;background:var(--brown);flex:none}
.brand-name{font-weight:600;color:var(--brown);font-size:26px;letter-spacing:-.5px;line-height:1}

/* letterhead */
.letterhead{left:60px;top:70px;width:450px;height:600px;display:flex;flex-direction:column}
.lh-head{display:flex;align-items:center;gap:14px;padding:34px 36px 0}
.lh-divider{width:1px;height:44px;background:var(--rule)}
.lh-contact{font-size:7.5px;line-height:1.45;color:var(--muted)}
.lh-contact strong{color:var(--ink);font-weight:600}
.lh-body{flex:1;padding:40px 40px 0 48px;font-size:8px;line-height:1.6;color:var(--muted)}
.lh-body p{margin-bottom:10px}
.lh-recipient{margin-bottom:16px}
.lh-footer{height:20px;background:var(--brown);color:#fff;font-size:7.5px;display:flex;align-items:center;padding-left:48px;letter-spacing:.3px}

/* business cards */
.card{width:300px;height:172px;border-radius:10px;overflow:hidden}
.card-front{display:flex;flex-direction:column}
.card-front .card-main{flex:1;display:flex;align-items:center;padding:0 20px;gap:14px}
.card-front .brand-name{font-size:22px}
.card-front .brand-dot{width:18px;height:18px}
.card-details{border-left:1px solid var(--rule);padding-left:12px;font-size:7.5px;line-height:1.5;color:var(--muted)}
.card-details .person{font-size:10px;font-weight:700;color:var(--copper)}
.card-details .role{font-size:8px;color:var(--ink);margin-bottom:4px}
.card-band{height:14px;background:var(--brown)}
.card-front-a{left:560px;top:70px}
.card-front-b{left:560px;top:270px}
.card-back-light{left:890px;top:70px;display:flex;align-items:center;justify-content:center}
.card-back-dark{left:890px;top:270px;background:linear-gradient(160deg,var(--slate),var(--slate-dark));display:flex;flex-direction:column;align-items:center;justify-content:center;gap:18px}
.card-back-dark .brand-name{color:#fff}
.card-back-dark .brand-dot{background:var(--copper)}
.card-url{font-size:8px;color:#e2e2e2;letter-spacing:.4px}

/* envelope */
.envelope{width:580px;height:190px;overflow:hidden}
.env-front{left:560px;top:470px}
.env-front .brand{position:absolute;left:26px;top:24px}
.env-front .brand-name{font-size:20px}
.env-front .brand-dot{width:16px;height:16px}
.env-address{position:absolute;left:26px;top:54px;font-size:7.5px;line-height:1.5;color:var(--muted)}
.env-band{position:absolute;left:0;right:0;bottom:0;height:16px;background:var(--brown)}
.env-back{left:560px;top:680px}
.env-back svg{position:absolute;inset:0}
.env-back .brand{position:absolute;left:50%;top:78px;transform:translateX(-50%)}
.env-back .brand-name{font-size:14px}
.env-back .brand-dot{width:12px;height:12px}
</style>
</head>
<body>
<main class="canvas">

  <!-- Letterhead -->
  <section class="sheet letterhead">
    <header class="lh-head">
      <div class="brand"><span class="brand-dot"></span><span class="brand-name">veradock</span></div>
      <div class="lh-divider"></div>
      <address class="lh-contact">
        <strong>4271 Harrowmill Road, Suite 100</strong><br>
        Oceanside CA, 92743<br>
        Phone: Use Place Holder<br>
        cdufresne@veradockpanes.example
      </address>
    </header>
    <div class="lh-body">
      <p>March 4, 2024</p>
      <p class="lh-recipient">Jordan Ellis<br>Project Coordinator<br>Northfield Builders<br>Portland OR, 97201</p>
      <p>Dear Jordan,</p>
      <p>Thank you for choosing our team for your upcoming window project. We are pleased to confirm the details of your order and the schedule for delivery and installation at your site.</p>
      <p>Each unit is built to order and inspected before it leaves our shop. Our crew will contact you a few days ahead to arrange a time that suits you.</p>
      <p>Please let us know if you have any questions in the meantime.</p>
      <p>Sincerely,<br><br>Calvin Dufresne<br>General Manager</p>
    </div>
    <footer class="lh-footer">www.veradockpanes.example</footer>
  </section>

  <!-- Business card fronts -->
  <section class="sheet card card-front card-front-a">
    <div class="card-main">
      <div class="brand"><span class="brand-dot"></span><span class="brand-name">veradock</span></div>
      <div class="card-details">
        <div class="person">Calvin Dufresne</div>
        <div class="role">General Manager</div>
        4271 Harrowmill Road, Suite 100<br>
        Oceanside CA, 92743<br>
        Phone: Use Place Holder<br>
        cdufresne@veradockpanes.example
      </div>
    </div>
    <div class="card-band"></div>
  </section>

  <section class="sheet card card-front card-front-b">
    <div class="card-main">
      <div class="brand"><span class="brand-dot"></span><span class="brand-name">veradock</span></div>
      <div class="card-details">
        <div class="person">Calvin Dufresne</div>
        <div class="role">General Manager</div>
        4271 Harrowmill Road, Suite 100<br>
        Oceanside CA, 92743<br>
        Phone: Use Place Holder<br>
        www.veradockpanes.example
      </div>
    </div>
    <div class="card-band"></div>
  </section>

  <!-- Business card backs -->
  <section class="sheet card card-back-light">
    <div class="brand"><span class="brand-dot"></span><span class="brand-name">veradock</span></div>
  </section>

  <section class="sheet card card-back-dark">
    <div class="brand"><span class="brand-dot"></span><span class="brand-name">veradock</span></div>
    <div class="card-url">www.veradockpanes.example</div>
  </section>

  <!-- Envelope front -->
  <section class="sheet envelope env-front">
    <div class="brand"><span class="brand-dot"></span><span class="brand-name">veradock</span></div>
    <address class="env-address">
      4271 Harrowmill Road, Suite 100<br>
      Oceanside CA, 92743
    </address>
    <div class="env-band"></div>
  </section>

  <!-- Envelope back -->
  <section class="sheet envelope env-back">
    <svg width="580" height="190" viewBox="0 0 580 190">
      <rect x="0" y="0" width="580" height="20" fill="var(--brown)"/>
      <polygon points="0,20 580,20 290,120" fill="#fafafa" stroke="#dcdcdc" stroke-width="1"/>
      <line x1="0" y1="190" x2="250" y2="100" stroke="#e4e4e4"/>
      <line x1="580" y1="190" x2="330" y2="100" stroke="#e4e4e4"/>
    </svg>
    <div class="brand"><span class="brand-dot"></span><span class="brand-name">veradock</span></div>
  </section>

</main>
</body>
</html>
```